Business Card Design Project (Beer industry)

I am seeking a redesign of my business card. I am looking for something that will really stand out in both texture and feel. Something more on the modern side then traditional. Nothing die cut shaped like a beer mug please.

The card is used mostly for other industry professionals, as well as bar and restaurant owners. My title is Strategy & Acquisitions. If you would like to somehow incorporate that theme, that may work.

My business is craft and imported beer. Nothing fizzy and yellow, so my products are more on the upscale side.
Updates

I was able to update my logo in .ai and .tif format. I hope that helps. 

Thank you all for your creative ideas. I have uploaded my current business card in pdf format, as well as our logo in .eps file format. We are excited about the submissions so far and want to thank you all again.

PS Please do not include fax number in future submissions, as we are looking for something more creative and a fax says 1999 and not 2015, which is the message we are going for, without being futuristic. 

Thank you all once again for all of your submissions. If we would consider a two sided card, we would like the opposite side not to be the same as the front. The styles we have seen so far, it appears the front and back are too similar. Again, a two sided card is not required. Thank you and we look forward to pushing the boundaries of your creativity. Cheers

Target Market(s)

My card would mostly go to bar and restaurant operators as well as other beer industry professionals

Industry/Entity Type

Restaurant

Requirements
Nice to have
• Two sided would be considered, although not required
Should not have
• Anything die cut shaped like a beer mug.

```html
<!DOCTYPE html>
<html lang="en">
<head>
<meta charset="utf-8">
<title>Harbor Tap Co. Business Card</title>
<link rel="stylesheet" href="https://fonts.googleapis.com/css2?family=PT+Sans:wght@400;700&family=Lora:ital,wght@1,400&display=swap">
<style>
  :root {
    --page-bg: #ece8e2;
    --wood-light: #e4d2b4;
    --wood-mid: #d6bf99;
    --wood-dark: #c5a87f;
    --plank-seam: rgba(120, 88, 50, 0.28);
    --grain: rgba(150, 115, 70, 0.10);
    --brand-blue: #1f4f8f;
    --brand-red: #9c1f24;
    --ink: #3b3128;
    --divider: #2c4d80;
  }
  * { box-sizing: border-box; margin: 0; padding: 0; }
  html, body {
    width: 1200px; height: 880px; overflow: hidden;
    background: var(--page-bg);
  }
  .canvas {
    width: 1200px; height: 880px;
    display: flex; flex-direction: column;
    align-items: center; justify-content: center; gap: 40px;
  }
  .card {
    position: relative;
    width: 700px; height: 400px;
    border-radius: 4px;
    overflow: hidden;
    box-shadow: 0 6px 18px rgba(60, 40, 20, 0.22);
  }
  .card-surface {
    position: absolute; inset: 0;
    background:
      repeating-linear-gradient(180deg, transparent 0 56px, var(--plank-seam) 56px 58px),
      repeating-linear-gradient(178deg, transparent 0 5px, var(--grain) 5px 6px, transparent 6px 13px),
      linear-gradient(100deg, var(--wood-light) 0%, var(--wood-mid) 40%, var(--wood-light) 68%, var(--wood-dark) 100%);
  }

  /* Front */
  .logo-lockup {
    position: relative; height: 100%;
    display: flex; flex-direction: column; align-items: center; justify-content: center;
    gap: 14px;
  }
  .brand-row { display: flex; align-items: center; gap: 14px; }
  .brand-dot {
    width: 34px; height: 34px; border-radius: 50%;
    background: var(--brand-red);
  }
  .brand-name {
    font-family: "PT Sans", sans-serif;
    font-weight: 700; font-size: 58px;
    color: var(--brand-red);
    letter-spacing: 1px;
  }
  .city {
    font-family: "Lora", serif; font-style: italic;
    font-size: 34px; color: var(--brand-blue);
    line-height: 1;
  }
  .tagline {
    font-family: "Lora", serif; font-style: italic;
    font-size: 19px; color: var(--ink);
  }

  /* Back */
  .card-back { display: flex; }
  .identity {
    position: relative;
    width: 50%;
    display: flex; flex-direction: column; justify-content: center;
    padding: 0 40px 0 56px;
    font-family: "PT Sans", sans-serif;
  }
  .person-name {
    font-size: 40px; font-weight: 700;
    color: var(--brand-blue);
    line-height: 1.1;
  }
  .person-title {
    font-size: 17px; margin-top: 8px; color: var(--ink);
  }
  .divider {
    position: relative;
    width: 2px; margin: 60px 0;
    background: var(--divider);
  }
  .contact {
    position: relative;
    flex: 1;
    display: flex; align-items: center;
    padding: 0 24px 0 36px;
    font-family: "PT Sans", sans-serif;
    color: var(--ink);
  }
  .contact-list { list-style: none; }
  .contact-list li {
    display: flex; align-items: center; gap: 12px;
    font-size: 17px; line-height: 34px;
  }
  .contact-icon { width: 16px; height: 16px; flex: none; }
  .contact-icon .fill { fill: var(--brand-blue); }
  .contact-icon .line { fill: none; stroke: var(--page-bg); stroke-width: 1.4; }
</style>
</head>
<body>
<main class="canvas">

  <section class="card card-front">
    <div class="card-surface" role="img" aria-label="Light bamboo wood plank texture"></div>
    <div class="logo-lockup">
      <div class="brand-row">
        <span class="brand-dot"></span>
        <span class="brand-name">Harbor Tap Co.</span>
      </div>
      <p class="city">New York</p>
      <p class="tagline">Premier Craft &amp; Import Beer Distributor</p>
    </div>
  </section>

  <section class="card card-back">
    <div class="card-surface" role="img" aria-label="Light bamboo wood plank texture"></div>
    <div class="identity">
      <h1 class="person-name">Name Surname</h1>
      <p class="person-title">Strategy &amp; Acquisitions</p>
    </div>
    <div class="divider"></div>
    <div class="contact">
      <ul class="contact-list">
        <li>
          <svg class="contact-icon" viewBox="0 0 16 16" aria-hidden="true"><rect class="fill" x="2" y="5" width="12" height="9" rx="2"/><rect class="fill" x="4" y="2" width="8" height="3" rx="1"/></svg>
          +00 123 456 789
        </li>
        <li>
          <svg class="contact-icon" viewBox="0 0 16 16" aria-hidden="true"><rect class="fill" x="4" y="1" width="8" height="14" rx="2"/></svg>
          +00 123 456 789
        </li>
        <li>
          <svg class="contact-icon" viewBox="0 0 16 16" aria-hidden="true"><rect class="fill" x="2" y="6" width="12" height="7" rx="1"/><rect class="fill" x="4" y="2" width="8" height="4"/></svg>
          +00 123 456 789
        </li>
        <li>
          <svg class="contact-icon" viewBox="0 0 16 16" aria-hidden="true"><rect class="fill" x="1" y="3" width="14" height="10" rx="1"/><path class="line" d="M1.5 4l6.5 5 6.5-5"/></svg>
          name.surname@domain.com
        </li>
        <li>
          <svg class="contact-icon" viewBox="0 0 16 16" aria-hidden="true"><circle class="fill" cx="8" cy="8" r="7"/><path class="line" d="M1 8h14M8 1c-3 3-3 11 0 14M8 1c3 3 3 11 0 14"/></svg>
          www.domain.com
        </li>
      </ul>
    </div>
  </section>

</main>
</body>
</html>
```